Packaging Design: Logo/Bottle Design for New Botanical Cocktail Brand

We are a new start up, looking to create a new line of Ready to drink Cocktails. The brand name is Verdelle Garden Cocktails, infused with fruit, herb, and floral botanicals grown on our farm in New Hampshire. Flavors will include: Herb flavored with cilantro, Berry- flavored with Alpine Strawberry, Citrus flavored with lemon Verbena & lemon balm, Pear flavored with Bartlett pear, Cucumber & Mint. We need a logo and a label design. There are 2 possible bottles to choose from.

Designer has complete freedom with everything! From fonts and colors to bottle caps and closures. Please view the pinterest link for inspirational bottle designs. https://www.pinboardly.example/kestrawynn/garden-drinks/

Target Market(s)

Female 21 to 48 years old. College educated and professional. The type of person that has a passion for a cause and eats and shops local. People that respect an artisan quality product, hand made by a master craftsman.

Industry/Entity Type

Floral

Requirements
Must have
• Clear Bottle, see options attached. You may also choose your own BUT WE MUST SEE THE LOGO AND IMAGERY ON A BOTTLE
• Logo Design: "Verdelle Garden Cocktails"
• Label: We can have front and back, or one continuous label. We are open to painted designs.
• The label must contain the following text in quotes:
• Product Name: " Verdelle Garden Cocktails "
• "15% Alc. by Vol. (30 proof)"
• "750 mL"
• "Handcrafted and Bottled by Harrow Creek Orchard Farm and Distillery
• Winchester, NH-USA"
• The following Text must be in all caps and 3mm in height:
• "Government Warning: (1) According to the Surgeon General, women should not drink alcoholic beverages during pregnancy because of the risk of birth defects. (2) Consumption of alcoholic beverages impairs your ability to drive a car or operate machinery and may cause health problems."
• Must be a space for a bar code: .75 in height by 1.25 in length.
• “www.harrowcreekorchard.example”
• Must Have the following Statement:
• Infused with fruit, herb, and floral botanicals and sweetened with stevia. Serve cold over ice.
Nice to have
• Antique or vintage botanical illustrations
• https://www.pinboardly.example/kestrawynn/garden-drinks/
• check out the board for inspiration.
• Think artisanal small batch spirits that are ready to drink out of the bottle. Refreshing flavors just pour over ice and add herb leaves.
• You can use images by doing a search here.
• http://archive.plantrecords.example/search.xhtml?start=0&collectionFacet=Orchard+Fruit+Painting+Set

```html
<!DOCTYPE html>
<html lang="en">
<head>
<meta charset="utf-8">
<title>Verdelle Garden Cocktails – Berry Label</title>
<link rel="stylesheet" href="https://fonts.googleapis.com/css2?family=Oswald:wght@400;500;600&family=Pinyon+Script&display=swap">
<style>
  :root {
    --backdrop: #050505;
    --label-white: #ffffff;
    --pink: #ee7d97;
    --pink-light: #f5a9ba;
    --pink-deep: #e46a86;
    --band-black: #0b0b0c;
    --rule-gold: #cbbd94;
    --cream: #e7dfcb;
    --ink: #2b2522;
    --berry-red: #c2403a;
    --berry-soft: #d98a7f;
  }
  * { margin: 0; padding: 0; box-sizing: border-box; }
  html, body {
    width: 1200px;
    height: 1000px;
    overflow: hidden;
    background: var(--backdrop);
  }
  .canvas {
    position: relative;
    width: 1200px;
    height: 1000px;
    background: var(--backdrop);
  }
  .label {
    position: absolute;
    left: 330px;
    top: 100px;
    width: 540px;
    height: 800px;
  }
  .label-shape {
    position: absolute;
    inset: 0;
    width: 540px;
    height: 800px;
  }
  .label-text {
    position: absolute;
    left: 0;
    width: 100%;
    text-align: center;
    font-family: "Oswald", sans-serif;
  }
  .brand-mark {
    top: 72px;
    font-size: 44px;
    font-weight: 600;
    letter-spacing: 6px;
    color: var(--label-white);
  }
  .product-script {
    top: 250px;
    font-family: "Pinyon Script", cursive;
    font-size: 118px;
    line-height: 1;
    color: var(--label-white);
  }
  .product-line {
    top: 440px;
    font-size: 31px;
    font-weight: 600;
    letter-spacing: 1px;
    color: var(--label-white);
  }
  .flavour-name {
    top: 546px;
    font-size: 25px;
    font-weight: 600;
    color: var(--ink);
  }
  .flavour-note {
    top: 582px;
    font-size: 20px;
    font-weight: 400;
    line-height: 1.25;
    color: var(--ink);
  }
  .fruit-illustration {
    position: absolute;
    left: 190px;
    top: 650px;
    width: 160px;
    height: 118px;
    border-radius: 10px;
    background: linear-gradient(160deg, var(--berry-soft), var(--berry-red));
  }
  .strength {
    position: absolute;
    left: 64px;
    top: 692px;
    font-family: "Oswald", sans-serif;
    font-size: 17px;
    line-height: 1.25;
    color: var(--ink);
    text-align: left;
  }
  .volume {
    position: absolute;
    left: 388px;
    top: 712px;
    font-family: "Oswald", sans-serif;
    font-size: 27px;
    color: var(--ink);
  }
</style>
</head>
<body>
<main class="canvas">
  <section class="label" aria-label="Verdelle Garden Cocktails Berry bottle label">
    <svg class="label-shape" viewBox="0 0 540 800" aria-hidden="true">
      <defs>
        <clipPath id="label-inner">
          <path d="M54,14 H486 A54,54 0 0 0 526,54 V746 A54,54 0 0 0 486,786 H54 A54,54 0 0 0 14,746 V54 A54,54 0 0 0 54,14 Z"/>
        </clipPath>
      </defs>
      <path class="label-border" fill="var(--label-white)"
            d="M40,0 H500 A40,40 0 0 0 540,40 V760 A40,40 0 0 0 500,800 H40 A40,40 0 0 0 0,760 V40 A40,40 0 0 0 40,0 Z"/>
      <g clip-path="url(#label-inner)">
        <rect class="cream-field" x="0" y="0" width="540" height="800" fill="var(--cream)"/>
        <rect class="pink-field" x="0" y="0" width="540" height="240" fill="var(--pink)"/>
        <rect class="pink-stripe" x="30" y="0" width="40" height="240" fill="var(--pink-light)"/>
        <rect class="pink-stripe" x="110" y="0" width="22" height="240" fill="var(--pink-deep)"/>
        <rect class="pink-stripe" x="150" y="0" width="30" height="240" fill="var(--pink-light)"/>
        <rect class="pink-stripe" x="360" y="0" width="30" height="240" fill="var(--pink-light)"/>
        <rect class="pink-stripe" x="408" y="0" width="22" height="240" fill="var(--pink-deep)"/>
        <rect class="pink-stripe" x="470" y="0" width="40" height="240" fill="var(--pink-light)"/>
        <path class="black-band" fill="var(--band-black)" d="M0,205 Q270,140 540,205 V522 H0 Z"/>
        <path class="band-rule" fill="none" stroke="var(--rule-gold)" stroke-width="2" d="M0,220 Q270,156 540,220"/>
        <line class="band-rule" x1="0" y1="508" x2="540" y2="508" stroke="var(--rule-gold)" stroke-width="1.5"/>
      </g>
    </svg>

    <div class="label-text brand-mark">VERDELLE</div>
    <div class="label-text product-script">Verdelle</div>
    <div class="label-text product-line">GARDEN COCKTAILS</div>
    <div class="label-text flavour-name">BERRY</div>
    <div class="label-text flavour-note">FLAVOURED WITH<br>ALPINE STRAWBERRY</div>
    <div class="fruit-illustration" role="img" aria-label="Vintage botanical illustration of alpine strawberries with leaves"></div>
    <div class="strength">15% ALC.<br>BY VOL.<br>(30 PROOF)</div>
    <div class="volume">750 mL</div>
  </section>
</main>
</body>
</html>
```